Quillon - Energy management company website design

We are interested in a total redesign of our website at www.quillonpowerco.co.uk. We are happy with our current colour scheme and logo but are ready for a new website.

The site is running on a CMS called Umbraco and will remain on this CMS. We are just looking for the html/css and js files so I can build the templates.

We are looking for a home page and maybe a couple of different types of content page. We would like the site to look clean and professional but not necessarily like every other corporate website.
We are really open to any design ideas, we've left the brief quite ambiguous for that reason. We are happy to consider any design no matter how unorthodox as long as it remains professional.

Target Market(s)

Large Businesses

Industry/Entity Type

It Company

Coding

Coded - Design and coding required

Number of Pages Required

3 page

Font styles to use
Sans Serif

Requirements
Must have
• We need a landing page designed and possibly two different kinds of content page allowing for different styles of content. We will want the css and js code with the pages.
• On the home page we would like Two prominent articles/products.
• Then a selection of our other products/services.
• Testimonials, Case studies and News Articles.
• Company colours:
• Text and topleft arrow blue (dark):
• R: 0 G: 96 B: 167
• Red Text and Arrow:
• R: 237 G: 27 B: 35
• Bottom left arrow blue (medium):
• R: 0 G: 174 B: 239
• Bottom right arrow blue (light):
• R: 171 G: 225 B: 250
Nice to have
• We are open to a potentially radical redesign of the site, it doesn't necessarily need to look like every other corporate website.
• We would like to see one or two designs base on this type of imagery:
• http://vuz.lk/PaRmet
• http://vuz.lk/3Hbxno
• http://vuz.lk/K4FUdj

```html
<!DOCTYPE html>
<html lang="en">
<head>
<meta charset="utf-8">
<title>Quillon – Integrated Energy Experts</title>
<link rel="stylesheet" href="https://fonts.googleapis.com/css2?family=Raleway:wght@300;400;500;600;700&display=swap">
<style>
:root{
  --blue-dark:#0060a7;
  --red:#ed1b23;
  --blue-mid:#00aeef;
  --blue-light:#abe1fa;
  --ink:#222;
  --text:#333;
  --grey-bg:#efefef;
  --card-head:#efefef;
  --card-border:#e2e2e2;
  --footer-bg:#eef1f4;
  --bar:#a9a9a9;
}
*{box-sizing:border-box;margin:0;padding:0}
html,body{width:1200px;height:2601px;overflow:hidden}
body{position:relative;background:#fff;font-family:"Raleway",Arial,sans-serif;color:var(--text)}
.abs{position:absolute}

/* header */
.top-rule{left:0;top:0;width:1200px;height:4px;background:var(--red)}
.site-header{left:0;top:4px;width:1200px;height:114px;background:#fff;border-bottom:5px solid var(--blue-dark)}
.brand{left:43px;top:26px;display:flex;align-items:center;gap:10px}
.brand-dot{width:40px;height:40px;border-radius:50%;background:var(--blue-dark)}
.brand-name{font-size:36px;font-weight:700;color:var(--blue-dark);letter-spacing:1px;line-height:1}
.brand-tag{font-size:12px;font-weight:700;color:var(--blue-dark);margin-top:3px}
.header-phone{right:48px;top:26px;font-size:13px;color:var(--ink);display:flex;align-items:center;gap:8px}
.main-nav{right:48px;top:74px;display:flex;gap:22px;font-size:13px;font-weight:700;color:var(--ink)}
.main-nav .active{color:var(--red)}

/* hero */
.hero{left:0;top:118px;width:1200px;height:602px;background:radial-gradient(ellipse at 55% 55%,#c9a27a 0%,#6a4a38 14%,#1c2a44 38%,#05070d 75%)}
.hero-title{left:0;top:185px;width:1200px;text-align:center;color:#fff;font-size:31px;font-weight:400;line-height:44px}
.hero-arrow{top:410px;width:28px;height:32px;background:#2a2418;border:1px solid #6b5a30;display:flex;align-items:center;justify-content:center}
.hero-call{left:83px;top:632px;color:#fff;font-size:32px;font-weight:500}

/* about */
.about{left:0;top:720px;width:1200px;height:350px;background:var(--grey-bg)}
.about-graphic{left:82px;top:788px;width:155px;height:180px;background:linear-gradient(135deg,#d6e6f3,#c7dbec)}
.about-title{left:343px;top:778px;font-size:32px;font-weight:400;color:var(--ink)}
.about-text{left:343px;top:827px;width:600px;font-size:12.5px;line-height:22px;color:var(--text)}
.btn{background:var(--red);color:#fff;font-size:13px;text-align:center;line-height:27px;height:27px}
.about-btn{left:343px;top:968px;width:125px}

/* services */
.section-title{left:0;width:1200px;text-align:center;font-size:32px;font-weight:400;color:var(--ink)}
.card{background:#fff;border:1px solid var(--card-border)}
.card-head{height:54px;background:var(--card-head);padding:0 18px;font-size:20px;line-height:54px;color:var(--ink)}
.card-img{left:12px;top:64px;width:97px;height:97px}
.card-text{left:125px;top:70px;width:170px;font-size:12.5px;line-height:16px;color:var(--text)}
.card-btn{right:0;bottom:0;width:102px}
.wide .card-text{width:355px}

.customers-head{display:flex;justify-content:space-between}
.customers-nav{color:#999;font-size:20px;letter-spacing:6px}
.client{font-size:17px;font-weight:700;color:var(--blue-dark)}

/* testimonials */
.quote{background:#eef1f5;border-bottom:2px solid var(--red)}
.quote-photo{left:0;top:0;width:178px;height:145px}
.quote-fold{left:127px;top:145px;width:51px;height:65px;background:#c8c8c8;clip-path:polygon(0 0,100% 0,100% 100%)}
.quote-text{left:200px;top:16px;width:270px;font-size:12.5px;line-height:16px;color:var(--text)}
.quote-who{left:200px;top:140px;font-size:12px;line-height:16px;font-style:italic;color:var(--ink)}
.quote-who b{font-weight:700}

/* footer */
.site-footer{left:0;top:2369px;width:1200px;height:194px;background:var(--footer-bg);border-top:2px solid var(--blue-mid)}
.footer-brand{left:43px;top:2390px}
.footer-address{left:83px;top:2457px;font-size:12.5px;line-height:17px;color:var(--ink)}
.social{top:2520px;width:25px;height:25px;border-radius:50%;background:#1b7fd1}
.footer-col{top:2397px;font-size:12.5px;line-height:17.5px;color:var(--ink)}
.footer-col h4{font-size:12.5px;font-weight:700;margin-bottom:5px}
.footer-map{left:880px;top:2420px;width:268px;height:120px;background:linear-gradient(135deg,#e9ebe2,#dfe6da 60%,#e8e1d3)}
.bottom-bar{left:0;top:2563px;width:1200px;height:38px;background:var(--bar);color:#fff;font-size:12.5px;line-height:38px;padding:0 43px;display:flex;justify-content:space-between}
</style>
</head>
<body>

<div class="abs top-rule"></div>
<header class="abs site-header"></header>
<div class="abs brand">
  <div class="brand-dot"></div>
  <div><div class="brand-name">QUILLON</div><div class="brand-tag">Integrated Energy Experts</div></div>
</div>
<div class="abs header-phone">
  <svg width="14" height="14" viewBox="0 0 24 24"><path fill="#111" d="M6.6 10.8a15 15 0 0 0 6.6 6.6l2.2-2.2a1 1 0 0 1 1-.25 11.4 11.4 0 0 0 3.6.57 1 1 0 0 1 1 1V20a1 1 0 0 1-1 1A17 17 0 0 1 3 4a1 1 0 0 1 1-1h3.5a1 1 0 0 1 1 1c0 1.25.2 2.45.57 3.6a1 1 0 0 1-.25 1z"/></svg>
  0845 210 7736
</div>
<nav class="abs main-nav">
  <span class="active">HOME</span><span>OUR SERVICES</span><span>OUR CUSTOMERS</span><span>PULSE</span><span>COMPANY</span><span>CONTACT US</span>
</nav>

<section class="abs hero" role="img" aria-label="A clenched fist gripping crackling blue and orange lightning on a dark background, with a 360 degree expertise emblem at lower right"></section>
<h1 class="abs hero-title">Quillon’s unique 360 degree service is designed<br>to optimise all areas of your energy and telecom expenditure</h1>
<div class="abs hero-arrow" style="left:33px"><svg width="10" height="14" viewBox="0 0 10 14"><path d="M8 1 2 7l6 6" stroke="#fff" stroke-width="2" fill="none"/></svg></div>
<div class="abs hero-arrow" style="left:1137px"><svg width="10" height="14" viewBox="0 0 10 14"><path d="M2 1l6 6-6 6" stroke="#fff" stroke-width="2" fill="none"/></svg></div>
<div class="abs hero-call">Call us on: 0845 210 7736</div>

<section class="abs about"></section>
<div class="abs about-graphic" role="img" aria-label="Service cycle graphic: compliance, procurement, efficiency and analysis"></div>
<h2 class="abs about-title">About Quillon</h2>
<p class="abs about-text">Lorem Ipsum is simply dummy text of the printing and typesetting industry. Lorem Ipsum has been the industry's standard dummy text ever since the 1500s, when ... unknown printer took a galley of type and scrambled it to make a type specimen book.Lorem Ipsum is simply dummy text of the printing and typesetting industry. Lorem Ipsum has been the industry's standard dummy text ever since the 1500s, when ... unknown printer took a galley of type and scrambled it to make a type specimen book.</p>
<div class="abs btn about-btn">Read More</div>

<h2 class="abs section-title" style="top:1135px">Our Services</h2>

<article class="abs card" style="left:81px;top:1214px;width:316px;height:217px">
  <div class="card-head">Energy Procurement</div>
  <div class="abs card-img" role="img" aria-label="Glowing light bulb" style="background:radial-gradient(circle,#9cc3e8,#1d3a5e 70%)"></div>
  <p class="abs card-text">Lorem Ipsum is simply dummy text of the printing and typesetting industry. Lorem Ipsum has been the industry's standard dummy text ever since the ...</p>
  <div class="abs btn card-btn">Read More</div>
</article>
<article class="abs card" style="left:437px;top:1214px;width:316px;height:217px">
  <div class="card-head">Energy Efficiency</div>
  <div class="abs card-img" role="img" aria-label="Electricity pylon against blue sky" style="background:linear-gradient(#3f86c8,#1d4f8a)"></div>
  <p class="abs card-text">Lorem Ipsum is simply dummy text of the printing and typesetting industry. Lorem Ipsum has been the industry's standard dummy text ever since the ...</p>
  <div class="abs btn card-btn">Read More</div>
</article>
<article class="abs card" style="left:791px;top:1214px;width:316px;height:217px">
  <div class="card-head">Energy Analysis</div>
  <div class="abs card-img" role="img" aria-label="Rising chart with gold highlight" style="background:linear-gradient(#555c66,#2c3036)"></div>
  <p class="abs card-text">Lorem Ipsum is simply dummy text of the printing and typesetting industry. Lorem Ipsum has been the industry's standard dummy text ever since the ...</p>
  <div class="abs btn card-btn">Read More</div>
</article>

<article class="abs card" style="left:81px;top:1467px;width:316px;height:219px">
  <div class="card-head">Energy Compliance</div>
  <div class="abs card-img" role="img" aria-label="Hand holding a glowing bulb" style="background:radial-gradient(circle,#6fa9d8,#0d1d33 70%)"></div>
  <p class="abs card-text">Lorem Ipsum is simply dummy text of the printing and typesetting industry. Lorem Ipsum has been the industry's standard dummy text ever since the ...</p>
  <div class="abs btn card-btn">Read More</div>
</article>
<article class="abs card" style="left:437px;top:1467px;width:316px;height:219px">
  <div class="card-head">Telecoms</div>
  <div class="abs card-img" role="img" aria-label="Desk telephone keypad" style="background:linear-gradient(135deg,#d9d9d9,#8a8a8a)"></div>
  <p class="abs card-text">Lorem Ipsum is simply dummy text of the printing and typesetting industry. Lorem Ipsum has been the industry's standard dummy text ever since the ...</p>
  <div class="abs btn card-btn">Read More</div>
</article>
<article class="abs card" style="left:791px;top:1467px;width:316px;height:219px">
  <div class="card-head">ESOS</div>
  <div class="abs card-img" role="img" aria-label="Satellite dish under a bright sky" style="background:linear-gradient(#8fb6dc,#d5e3ef)"></div>
  <p class="abs card-text">Lorem Ipsum is simply dummy text of the printing and typesetting industry. Lorem Ipsum has been the industry's standard dummy text ever since the ...</p>
  <div class="abs btn card-btn">Read More</div>
</article>

<article class="abs card wide" style="left:81px;top:1720px;width:502px;height:217px">
  <div class="card-head">Public Sector</div>
  <div class="abs card-img" role="img" aria-label="Hands holding banknotes" style="background:linear-gradient(135deg,#b9c5a8,#4d5a44)"></div>
  <p class="abs card-text">Lorem Ipsum is simply dummy text of the printing and typesetting industry. Lorem Ipsum has been the industry's standard dummy text ever since the 1500s, when ... unknown printer took a galley of type and scrambled it to make a type specimen book.Lorem Ipsum is simply dummy text of the printing and typesetting industry.</p>
  <div class="abs btn card-btn">Read More</div>
</article>
<article class="abs card" style="left:605px;top:1720px;width:502px;height:217px">
  <div class="card-head customers-head"><span>Our Customers</span><span class="customers-nav">‹ ›</span></div>
  <div class="abs client" style="left:28px;top:88px">Larkfield Airport</div>
  <div class="abs client" style="left:185px;top:88px">Ostrand</div>
  <div class="abs client" style="left:362px;top:88px">Hollins</div>
  <div class="abs client" style="left:28px;top:150px">Brenhauser</div>
  <div class="abs client" style="left:185px;top:150px">Kestrel Glass</div>
  <div class="abs client" style="left:362px;top:150px">Marrow Group</div>
</article>

<h2 class="abs section-title" style="top:2018px">Customer Testimonials</h2>

<article class="abs quote" style="left:83px;top:2098px;width:496px;height:212px">
  <div class="abs quote-photo" role="img" aria-label="Portrait of a smiling man" style="background:linear-gradient(#a9927a,#d8d3cc)"></div>
  <div class="abs quote-fold"></div>
  <p class="abs quote-text">Quillon listened to our needs and delivered a service that was tailored to us. The strategic management of our flexible purchasing contracts has been a great success, their energy conservation expertise has helped us enormously, and we'd have no hesitation recommending their services.</p>
  <p class="abs quote-who"><b>Daniel Hurst</b><br>Stadium Manager<br>Riverside Athletic Club</p>
</article>
<article class="abs quote" style="left:610px;top:2098px;width:497px;height:212px">
  <div class="abs quote-photo" role="img" aria-label="Portrait of a smiling woman" style="background:linear-gradient(#e6e2de,#cfc4ba)"></div>
  <div class="abs quote-fold"></div>
  <p class="abs quote-text">Quillon listened to our needs and delivered a service that was tailored to us. The strategic management of our flexible purchasing contracts has been a great success, their energy conservation expertise has helped us enormously, and we'd have no hesitation recommending their services.</p>
  <p class="abs quote-who"><b>Clara Novik</b><br>Stadium Manager<br>Riverside Athletic Club</p>
</article>

<footer class="abs site-footer"></footer>
<div class="abs brand footer-brand">
  <div class="brand-dot"></div>
  <div><div class="brand-name">QUILLON</div><div class="brand-tag">Integrated Energy Experts</div></div>
</div>
<p class="abs footer-address">Quillon Utilities Ltd<br>Quillon House, Marsh Lane<br>Fleetmoor, FM2 8QT</p>
<div class="abs social" style="left:83px" aria-label="Social profile"></div>
<div class="abs social" style="left:115px" aria-label="Social profile"></div>
<div class="abs footer-col" style="left:484px"><h4>Navigations</h4>About Us<br>Our Customers<br>Quillon Energy View<br>Contact Us</div>
<div class="abs footer-col" style="left:667px"><h4>Our Services</h4>Energy Procurement<br>Energy Efficiency<br>Energy Analysis<br>Energy Compliance<br>Telecoms<br>ESOS<br>Public Sector</div>
<div class="abs footer-col" style="left:880px"><h4>Our Location</h4></div>
<div class="abs footer-map" role="img" aria-label="Street map showing the office location"></div>
<div class="abs bottom-bar"><span>© 2013 Quillon Utilities Limited</span><span>Privacy Policy &nbsp;|&nbsp; Disclaimer</span></div>

</body>
</html>
```